Packaging Design for Vorimelt a Company Providing a Convenient and Complete Alternative to Food

We need a packaging and label design for Vorimelt. Vorimelt stands for nutrient balance and it is a meal alternative that comes in a powder that has all the nutrients needed for a complete and balanced meal. Vorimelt would be used by people that are hungry but don't have time to cook, are in a rush, or simply want to get the healthiest meal they can as conveniently as possible. We were thinking of using a modern and simple design that would attract consumers in the 22-28 age bracket. I want the packaging to be cool and attractive using blue and orange/red (an orangey red) since those are the colors of the logo

Now that being said, Vorimelt is more about a lifestyle than the product itself. The website still doesn't reflect this because the first step for me in creating it was to put in all the hard info and facts and then slowly transform it to what I want it to be. Vorimelt's "slogan" is spark every hour and the idea is that the product will be used by people who are busy having too much fun in life so they don't have time to cook so they choose to have Vorimelt. For example a commercial we are producing starts with first person footage of me getting in a skyvane 40 and then doing all sorts of water sports and having fun in the beach. At the end, there's a hot girl in a boat making a vorimelt and drinking it. So as you can see it's not about the product itself but what we want people to feel when they think about it and part of what they feel will be conveyed by the logo.

I want to convey a sense of energy and fun. I want people to feel inspired and feel something when they see the packaging since this is the same logo that will go on the product packaging (I will hold another project for that as soon as this one ends).

Our target market is a young professional probably with higher disposable income than your average 24-35 year old, trendy, modern, sophisticated and often consumes premium brands and therefore the packaging must reflect that.

The bottle will use a shrink sleeve that will wrap around from the bottom of the bottle up to the neck. The bottle is white, with a white smooth cap. I want the design to be able to blend in with the white of the bottle so that it all flows. I was thinking of maybe leaving some parts transparent so that the white of the bottle shows instead of using white but I honestly don't know if that would be a good idea.

Attached you will find the template for the shrink sleeve, the logo and the tub. The picture of the bottle is only a reference so that you can know what size it will be.

I'm going to need the design both in the template and on the tub. Make it look nice since I might be using the designs as a background in the website and definitely as the product image (what people will be clicking on to buy it)

Here are the things that need to be on the tub (these will be modified later only to be used as a placeholder for now):

Under the logo or in the front and middle of the tub (under Vorimelt probably):
A Complete and Balanced Meal Alternative.

It needs to say its vanilla flavored

It needs to have the supplement facts (just put any random numbers)

Directions: Use 2-4 scoops depending on your level of hunger. Mix 5 ounces of water per scoop in a thermos, shaker cup, or closed bottle and shake vigorously for ten seconds. Drink and enjoy!

What is Vorimelt?
Vorimelt is a complete and balanced meal alternative that gives your body all the right nutrients to keep it functioning at its full potential. Vorimelt will nourish your body with good proteins, carbohydrates, fats, and micro-nutrients (like vitamins and minerals) so that you don't have to worry about cooking or eating the right stuff. We take care of everything for you so that you can keep on doing what you love, whatever that may be. Vorimelt will spark every hour!
For more information go to Vorimelt.example

Hey i forgot to add that its gonna be vanilla flavored

```html
<!DOCTYPE html>
<html lang="en">
<head>
<meta charset="utf-8">
<title>Vorimelt Tub Label – Vanilla</title>
<link href="https://fonts.googleapis.com/css2?family=Roboto:wght@400;500;700;900&family=Open+Sans:wght@400;600;700&display=swap" rel="stylesheet">
<style>
  :root{
    --page-bg:#e9e9ea;
    --label-bg:#f7f8f9;
    --brand-blue:#2b7fcb;
    --deep-blue:#1550b4;
    --band-blue:#2f8fd9;
    --accent-orange:#e8562a;
    --ink:#262a30;
    --muted:#5d636b;
    --rule:#1d1f22;
  }
  *{box-sizing:border-box;margin:0;padding:0}
  html,body{width:1200px;height:960px;overflow:hidden}
  body{background:var(--page-bg);font-family:"Open Sans",Arial,sans-serif;color:var(--ink);position:relative}

  .label{
    position:absolute;left:50px;top:190px;width:1100px;height:580px;
    background:var(--label-bg);display:flex;
    box-shadow:0 1px 3px rgba(0,0,0,.08);
  }
  .panel{position:relative;height:100%}
  .panel--side{width:330px;padding:48px 30px 0}
  .panel--front{width:440px;text-align:center;padding-top:62px}

  /* left side */
  .body-copy{font-size:11px;line-height:1.6;text-align:justify;color:var(--ink);margin-bottom:14px}
  .caps-copy{font-size:10.5px;line-height:1.6;text-transform:uppercase;text-align:justify;margin-bottom:18px}
  .side-heading{font-family:"Roboto",Arial,sans-serif;font-weight:700;font-size:13px;margin-bottom:10px}
  .side-brand{margin-top:22px;display:flex;align-items:center;gap:8px}
  .side-url{font-family:"Roboto",Arial,sans-serif;font-weight:700;font-size:13px;margin-top:14px}

  /* logo lockup */
  .brand{display:inline-flex;align-items:center;gap:8px}
  .brand__dot{width:34px;height:34px;border-radius:50%;background:var(--accent-orange)}
  .brand__dot--small{width:22px;height:22px}
  .brand__name{font-family:"Roboto",Arial,sans-serif;font-weight:500;font-size:27px;letter-spacing:.5px;color:var(--brand-blue)}
  .brand__name--small{font-size:17px}
  .brand-tagline{display:block;font-family:"Roboto",Arial,sans-serif;font-size:10px;font-weight:500;color:var(--accent-orange);text-align:right;width:230px;margin:-4px auto 0;padding-right:6px}

  /* front */
  .headline{font-family:"Roboto",Arial,sans-serif;color:var(--brand-blue);margin-top:44px;line-height:1.2}
  .headline__lead{display:block;font-size:23px;font-weight:500}
  .headline__main{display:block;font-size:34px;font-weight:500}
  .flavor-badge{
    display:inline-block;margin-top:18px;padding:8px 14px;border-radius:4px;
    background:linear-gradient(180deg,#3a92dd,#2270c0);color:#fff;
    font-family:"Roboto",Arial,sans-serif;font-weight:700;font-size:22px;letter-spacing:.3px
  }
  .hca-seal{
    width:96px;height:96px;border-radius:50%;margin:22px auto 0;
    background:var(--band-blue);color:#fff;display:flex;flex-direction:column;justify-content:center;
    font-family:"Roboto",Arial,sans-serif;font-weight:700;font-size:25px;line-height:1.05;transform:rotate(-12deg)
  }
  .front-sub{font-family:"Roboto",Arial,sans-serif;font-weight:700;color:var(--brand-blue);font-size:13px;letter-spacing:1.6px;margin-top:30px}
  .front-fine{font-family:"Roboto",Arial,sans-serif;font-weight:700;color:var(--brand-blue);font-size:7px;letter-spacing:.6px;margin-top:8px}

  .base-band{position:absolute;left:0;right:0;bottom:30px;height:32px}
  .base-band__line{height:6px;background:var(--deep-blue)}
  .base-band__fill{height:26px;background:linear-gradient(90deg,var(--band-blue),#3d9be2,var(--band-blue))}

  /* right side */
  .facts{border:2px solid var(--rule);padding:8px 10px;font-family:"Roboto",Arial,sans-serif;font-size:10.5px;background:#fff}
  .facts__title{font-weight:900;font-size:24px;line-height:1;margin-bottom:4px}
  .facts__row{display:flex;justify-content:space-between;padding:2px 0}
  .facts__rule{border-top:6px solid var(--rule);margin:4px 0}
  .facts__thin{border-top:1px solid var(--rule)}
  .facts__note{font-size:9px;margin-top:4px}
  .about-copy{font-size:11px;line-height:1.6;margin-top:16px}
  .about-caps{font-family:"Roboto",Arial,sans-serif;font-weight:700;font-size:11px;margin-top:12px;text-transform:uppercase}
</style>
</head>
<body>
<main class="label">

  <section class="panel panel--side panel--info">
    <p class="body-copy">Lorem ipsum dolor sit amet, consectetur adipisicing elit, sed do eiusmod tempor incididunt ut labore et dolore magna aliqua. Ut enim ad minim veniam, quis nostrud exercitation lorem ipsum dolor sit amet, consectetur adipisicing elit, sed do eiusmod tempor incididunt ut labore et dolore magna aliqua exercitation.</p>
    <p class="body-copy">Lorem ipsum dolor sit amet, consectetur adipisicing elit, sed do eiusmod tempor incididunt ut labore et dolore. Ut enim ad minim veniam, quis nostrud exercitation ullamco, consectetur adipisicing elit, sed do eiusmod tempor dolore magna aliqua. Lorem ipsum dolor.</p>
    <p class="caps-copy">Lorem ipsum dolor sit amet, consectetur adipisicing elit, sed do eiusmod tempor incididunt ut labore et dolore magna aliqua.</p>
    <h2 class="side-heading">WHAT IS VORIMELT?</h2>
    <p class="caps-copy">Lorem ipsum dolor sit amet, consectetur adipisicing elit, sed do lorem ipsum dolor sit amet, consectetur adipisicing elit,</p>
    <div class="side-brand brand">
      <span class="brand__dot brand__dot--small"></span>
      <span class="brand__name brand__name--small">VORIMELT</span>
    </div>
    <p class="side-url">Vorimelt.example</p>
  </section>

  <section class="panel panel--front">
    <div class="brand">
      <span class="brand__dot"></span>
      <span class="brand__name">VORIMELT</span>
    </div>
    <span class="brand-tagline">Spark every hour!</span>

    <h1 class="headline">
      <span class="headline__lead">A Complete and Balanced</span>
      <span class="headline__main">Meal Alternative</span>
    </h1>

    <div class="flavor-badge">VANILLA FLAVORED</div>

    <div class="hca-seal"><span>65%</span><span>HCA</span></div>

    <p class="front-sub">LOREM IPSUM DOLOR SIT AMET</p>
    <p class="front-fine">LOREM IPSUM DOLOR SIT AMET, CONSECTETUR ADIPISICING ELIT, SED DO EIUSMOD TEMPO</p>
  </section>

  <section class="panel panel--side panel--facts">
    <div class="facts">
      <div class="facts__title">Supplement Facts</div>
      <div class="facts__row"><span>Serving Size 2 Scoops (60g)</span></div>
      <div class="facts__row"><span>Servings Per Container 20</span></div>
      <div class="facts__rule"></div>
      <div class="facts__row"><strong>Amount Per Serving</strong><strong>% Daily Value</strong></div>
      <div class="facts__thin"></div>
      <div class="facts__row"><span>Calories 240</span><span></span></div>
      <div class="facts__thin"></div>
      <div class="facts__row"><span>Total Fat 9g</span><span>12%</span></div>
      <div class="facts__thin"></div>
      <div class="facts__row"><span>Protein 20g</span><span>40%</span></div>
      <div class="facts__rule"></div>
      <p class="facts__note">* Daily Value not established.</p>
    </div>
    <p class="about-copy">Vorimelt is a complete and balanced meal alternative that gives your body all the right nutrients to keep it functioning at its full potential. Vorimelt will nourish your body with good proteins, carbohydrates, fats, and micro-nutrients (like vitamins and minerals) so that you don't have to worry about cooking or eating the right stuff. We take care of everything for you so that you can keep on doing what you love. Vorimelt will spark every hour!</p>
    <p class="about-caps">Lorem ipsum dolor sit amet</p>
  </section>

  <div class="base-band" aria-hidden="true">
    <div class="base-band__line"></div>
    <div class="base-band__fill"></div>
  </div>
</main>
</body>
</html>
```